Talvane Companies Business Card Design

We need a new business card for our Private Equity Real Estate Development firm, “Talvane” and our EB-5 regional center “Moorfield Regional Center” on one card. We prefer a design that is simple, elegant, and represents the luxury products we design and build as well as the financial security and stability our successful history has produced. We are an industry leader in our field and 3rd generation family business that has evolved into an institutional quality investment platform. Considered design size is standard business card dimensions (3.5 x 2 inches with an additional 1/8 inch space for design elements or backgrounds that extend beyond the finished size of your piece.

Target Market(s)

• High net worth individuals
• Highly skilled technical workers and physicians in the US seeking investment-based immigration opportunities
• Sophisticated private equity investors
• Intermediary partners include domestic attorneys and investment brokers, as well as international agent networks
• US real estate developers

Industry/Entity Type

Finance

Contact Information for Business Card

(Providing placeholder info for personal information, please design for longer character spaces, longer names and addresses etc..)
• Logo for Talvane
• Logo for Moorfield Regional Center
• Full name: Dorian Talvane
• Job title: CEO
• Email address: dtalvane@talvanecompanies.example
• Cell phone number: +1.555.318.4476
• Office number +1.555.240.6185
• Office address: Quillan Court 5, 4817 Vista Ardell, Larkhaven, OR.
• Website: www.talvanecompanies.example

Font styles to use
Serif
Sans Serif

Colors
ec1f27
ffffff
000000

Requirements
Must have
• • Logo for Talvane
• • Logo for Moorfield Regional Center
• - Use rounded corners
• (See .ai file included for logos)
Nice to have
• • Simple, elegant design
• • Aesthetically compatible with our website design (www.talvanecompanies.example)
• • Color palette including but not limited to white, black, and red (as per logos)
Should not have
• - Not too much red color
• - Do not stack both logos on top of each other

```html
<!DOCTYPE html>
<html lang="en">
<head>
<meta charset="utf-8">
<title>Talvane Companies Business Card</title>
<link rel="stylesheet" href="https://fonts.googleapis.com/css2?family=Poppins:wght@300;400;600;700&display=swap">
<style>
  :root {
    --bg: #a3b6b0;
    --card: #ffffff;
    --ink: #1e1e1e;
    --black: #1d1d1b;
    --red: #a61c2e;
    --grey: #4a4a4a;
    --white: #ffffff;
  }
  * { margin: 0; padding: 0; box-sizing: border-box; }
  html, body {
    width: 1200px; height: 1029px; overflow: hidden;
    background: var(--bg);
    font-family: "Poppins", sans-serif;
  }
  .card {
    position: absolute;
    width: 660px; height: 377px;
    left: 270px;
    background: var(--card);
    border-radius: 14px;
    overflow: hidden;
    box-shadow: 0 12px 30px rgba(0,0,0,0.18);
  }
  .card-front { top: 90px; }
  .card-back { top: 552px; }
  .card-art { position: absolute; inset: 0; width: 100%; height: 100%; }

  /* front */
  .holder { position: absolute; left: 48px; top: 166px; padding-left: 14px; border-left: 5px solid var(--red); }
  .holder-name { color: var(--white); font-size: 25px; line-height: 1.1; letter-spacing: 0.2px; white-space: nowrap; }
  .holder-name strong { font-weight: 700; }
  .holder-name span { font-weight: 300; }
  .holder-title { color: var(--white); font-size: 14px; font-weight: 400; margin-top: 6px; }

  .center-mark { position: absolute; left: 458px; top: 96px; display: flex; align-items: center; gap: 10px; }
  .center-mark-square { width: 22px; height: 22px; background: var(--red); flex: none; }
  .center-mark-name { color: var(--white); font-weight: 600; font-size: 19px; line-height: 1.15; letter-spacing: 1px; white-space: nowrap; }
  .center-mark-name small { display: block; font-size: 10px; letter-spacing: 3px; }

  .contacts { position: absolute; left: 48px; top: 268px; list-style: none; }
  .contacts li { display: flex; align-items: flex-start; gap: 10px; color: var(--ink); font-size: 13px; font-weight: 400; line-height: 1.35; margin-bottom: 3px; white-space: nowrap; }
  .contacts li.address { margin-top: 6px; }
  .contact-icon { width: 15px; height: 15px; flex: none; margin-top: 2px; }

  /* back */
  .brand { position: absolute; left: 0; right: 0; top: 140px; display: flex; flex-direction: column; align-items: center; }
  .brand-row { display: flex; align-items: center; gap: 14px; }
  .brand-square { width: 30px; height: 30px; background: var(--grey); }
  .brand-name { color: var(--grey); font-size: 34px; font-weight: 600; letter-spacing: 3px; line-height: 1; }
  .brand-name small { display: block; font-size: 13px; letter-spacing: 10px; margin-top: 6px; text-align: right; }
  .website { margin-top: 30px; color: var(--ink); font-size: 13px; }
  .website span { color: var(--red); }
</style>
</head>
<body>

<section class="card card-front">
  <svg class="card-art" viewBox="0 0 660 377" aria-hidden="true">
    <path fill="var(--red)" d="M0,122 H215 Q258,122 270,146 H0 Z"/>
    <path fill="var(--red)" d="M0,232 H360 C410,232 420,176 470,176 H500 C450,176 440,254 365,254 H0 Z"/>
    <path fill="var(--black)" d="M0,146 H250 C300,146 312,62 372,62 H660 V176 H480 C430,176 418,238 362,238 H0 Z"/>
  </svg>

  <div class="holder">
    <p class="holder-name"><strong>DORIAN</strong> <span>TALVANE</span></p>
    <p class="holder-title">CEO</p>
  </div>

  <div class="center-mark">
    <div class="center-mark-square"></div>
    <p class="center-mark-name">MOORFIELD<small>REGIONAL CENTER</small></p>
  </div>

  <ul class="contacts">
    <li>
      <svg class="contact-icon" viewBox="0 0 16 16"><circle cx="8" cy="8" r="8" fill="var(--ink)"/><rect x="5.5" y="3.5" width="5" height="9" rx="1" fill="none" stroke="#fff" stroke-width="1.2"/></svg>
      +1.555.318.4476
    </li>
    <li>
      <svg class="contact-icon" viewBox="0 0 16 16"><circle cx="8" cy="8" r="8" fill="var(--ink)"/><path d="M5,4.5 L6.6,4.5 L7.2,6.5 L6.3,7.3 Q7.2,9 8.8,9.8 L9.6,8.9 L11.5,9.5 L11.5,11 Q8,11.5 5.5,8 Q4.5,6 5,4.5 Z" fill="#fff"/></svg>
      +1.555.240.6185
    </li>
    <li>
      <svg class="contact-icon" viewBox="0 0 16 16"><circle cx="8" cy="8" r="8" fill="var(--ink)"/><rect x="4" y="5" width="8" height="6" fill="none" stroke="#fff" stroke-width="1.1"/><path d="M4,5 L8,8.3 L12,5" fill="none" stroke="#fff" stroke-width="1.1"/></svg>
      dtalvane@talvanecompanies.example
    </li>
    <li class="address">
      <svg class="contact-icon" viewBox="0 0 16 16"><circle cx="8" cy="8" r="8" fill="var(--ink)"/><path d="M8,3.5 C5.9,3.5 4.8,5 4.8,6.6 C4.8,8.8 8,12.5 8,12.5 C8,12.5 11.2,8.8 11.2,6.6 C11.2,5 10.1,3.5 8,3.5 Z" fill="#fff"/><circle cx="8" cy="6.6" r="1.2" fill="var(--ink)"/></svg>
      <span>Quillan Court 5, 4817 Vista Ardell,<br>Larkhaven, OR.</span>
    </li>
  </ul>
</section>

<section class="card card-back">
  <svg class="card-art" viewBox="0 0 660 377" aria-hidden="true">
    <polygon fill="var(--red)" points="560,0 620,0 660,40 660,110"/>
    <polygon fill="var(--black)" points="620,0 660,0 660,40"/>
    <polygon fill="var(--red)" points="0,250 0,377 95,377 0,300"/>
    <path fill="var(--red)" d="M0,230 Q20,230 40,250 L150,377 H95 L0,300 Z"/>
    <polygon fill="var(--black)" points="95,377 0,300 0,340 45,377"/>
  </svg>

  <div class="brand">
    <div class="brand-row">
      <div class="brand-square"></div>
      <p class="brand-name">TALVANE<small>CAPITAL</small></p>
    </div>
    <p class="website">www.<span>talvanecompanies</span>.example</p>
  </div>
</section>

</body>
</html>
```